Holistic Financial Planning Practice

I need a business card design and logo for my Financial Planning Practice(Wren Financial Planning).

Wren(Wisdom, Reliability and Esteem) Financial Planning provides service to both individuals, companies, self managed super funds on wide range of advice. Wren Financial Planning is licensed through KVL.

I have attached an existing business card which needs up-dating

Wren's webpage provides a good overview of what I do which is www.wrenvq.com.au

All the KVL branding needs to be included, including 'Wren Financial Planning is an Authorised Representative of Korvel Financial Planning Pty Limited ABN 38207 941 562 ACN 207 941 562'

An idea.......At Wren It's the sense that make the dollars.

Industry/Entity Type

Business

Contact Information for Business Card

Wren Financial Planning, Dorian Fassett MFS(FP), B.Bus, ADFS ; Suite 304, Level 3, 57 Tamsin Street Kogarah NSW 2217 Australia
Ph: 02 9370 4165 Fax 02 9743 2051 Mobile 04153 70926 Email dorian@wrenvq.com.au Web www.wrenvq.com.au

```html
<!DOCTYPE html>
<html lang="en">
<head>
<meta charset="utf-8">
<title>Wren Financial Planning – Business Card</title>
<link rel="stylesheet" href="https://fonts.googleapis.com/css2?family=Open+Sans:wght@400;600;700&family=Roboto+Slab:wght@400;700&display=swap">
<style>
  :root {
    --backdrop: #cbcbcb;
    --card: #f4f4f2;
    --navy: #3d4a85;
    --ink: #1f2540;
    --rule: #6a6f85;
  }
  html, body {
    margin: 0;
    padding: 0;
    width: 1200px;
    height: 1001px;
    overflow: hidden;
    background: var(--backdrop);
  }
  .canvas {
    width: 1200px;
    height: 1001px;
    display: flex;
    align-items: center;
    justify-content: center;
  }
  .card {
    position: relative;
    width: 880px;
    height: 538px;
    background: var(--card);
    box-shadow: 0 2px 6px rgba(0,0,0,0.18);
    color: var(--navy);
    font-family: "Open Sans", Arial, sans-serif;
  }
  .brand {
    position: absolute;
    left: 56px;
    top: 60px;
    display: flex;
    align-items: center;
    gap: 18px;
  }
  .brand-mark {
    width: 58px;
    height: 58px;
    background: var(--navy);
  }
  .brand-name {
    font-weight: 700;
    font-size: 34px;
    letter-spacing: 1px;
    text-transform: uppercase;
    color: var(--navy);
  }
  .person {
    position: absolute;
    left: 56px;
    top: 168px;
  }
  .person-name {
    font-weight: 700;
    font-size: 26px;
    margin: 0;
  }
  .person-quals {
    font-size: 21px;
    margin: 2px 0 18px;
  }
  .address, .contact {
    font-size: 17px;
    line-height: 1.35;
    margin: 0 0 16px;
  }
  .contact span { display: inline-block; width: 30px; }
  .licensing {
    position: absolute;
    right: 56px;
    top: 200px;
    text-align: right;
    font-size: 14px;
    line-height: 1.45;
  }
  .licensing .spaced { letter-spacing: 4px; }
  .accreditation {
    position: absolute;
    right: 56px;
    top: 330px;
    display: flex;
    align-items: center;
    gap: 16px;
  }
  .accredited-by {
    font-family: "Roboto Slab", Georgia, serif;
    text-align: right;
    color: var(--ink);
    font-size: 20px;
    line-height: 1.2;
  }
  .accredited-by strong { display: block; font-weight: 700; }
  .divider {
    width: 1px;
    height: 56px;
    background: var(--rule);
  }
  .partner-name {
    font-family: "Open Sans", Arial, sans-serif;
    font-weight: 700;
    font-size: 32px;
    color: var(--ink);
  }
  .partner-dot {
    width: 26px;
    height: 26px;
    border-radius: 50%;
    background: #6fa6d8;
  }
</style>
</head>
<body>
<main class="canvas">
  <article class="card">
    <header class="brand">
      <div class="brand-mark" aria-hidden="true"></div>
      <div class="brand-name">Wren Financial Planning</div>
    </header>

    <section class="person">
      <h1 class="person-name">Dorian Fassett</h1>
      <p class="person-quals">MFS(FP), B.Bus, ADFS</p>
      <p class="address">Suite 304, Level 3<br>57 Tamsin Street<br>Kogarah NSW 2217<br>Australia</p>
      <p class="contact">
        <span>P:</span>02 9370 4165<br>
        <span>F:</span>02 9743 2051<br>
        <span>M:</span>04 153 70926<br>
        <span>E:</span>dorian@wrenvq.com.au<br>
        <span>W:</span>www.wrenvq.com.au
      </p>
    </section>

    <section class="licensing">
      <div class="spaced">Wren Financial Planning is an</div>
      <div class="spaced">Authorised Representative</div>
      <div>of Korvel Financial Planning Pty Limited</div>
      <div>ABN 38207 941 562 ACN 207 941 562</div>
    </section>

    <section class="accreditation">
      <div class="accredited-by">Accredited by<strong>KVL Financial Planning</strong></div>
      <div class="divider" aria-hidden="true"></div>
      <div class="partner-name">KVL</div>
      <div class="partner-dot" aria-hidden="true"></div>
    </section>
  </article>
</main>
</body>
</html>
```